Business Card for Industrial Distributor

We need a business card design for an industrial distributor. We sell machine parts for the manufacturing and oil industry. We would like the cards to look clean and modern but with a touch of industry.

Our colors are blue/white.

Please feel free to visit our website www.krovelmint.com

Target Market(s)

mexican manufacturers in the automobile/aerospace industry

Industry/Entity Type

Industrial

Colors
ffffff
0555a3

```html
<!DOCTYPE html>
<html lang="en">
<head>
<meta charset="utf-8">
<title>Krovelmint Business Card</title>
<link href="https://fonts.googleapis.com/css2?family=Montserrat:wght@400;500;600;800&display=swap" rel="stylesheet">
<style>
  :root {
    --page-bg: #2a2a2c;
    --card-black: #000000;
    --band-blue: #2b3aa2;
    --accent-line: #1a8fe0;
    --text-blue: #1c82d8;
    --mark-blue: #3442b8;
    --mark-circle: #1f66c8;
    --ghost-circle: #0a1026;
    --white: #ffffff;
    --soft-white: #e8e8ec;
  }
  * { margin: 0; padding: 0; box-sizing: border-box; }
  html, body {
    width: 1200px; height: 900px; overflow: hidden;
    background: var(--page-bg);
    font-family: "Montserrat", sans-serif;
  }
  .canvas { position: relative; width: 1200px; height: 900px; }
  .card {
    position: absolute;
    width: 600px; height: 343px;
    background: var(--card-black);
    border-radius: 18px;
    overflow: hidden;
    box-shadow: 0 14px 30px rgba(0,0,0,.55);
  }
  /* Back of card */
  .card-back { left: 80px; top: 110px; }
  .back-mark {
    position: absolute; left: 0; right: 0; top: 62px;
    display: flex; flex-direction: column; align-items: center; gap: 14px;
  }
  .back-mark .mark-circle {
    width: 130px; height: 130px; border-radius: 50%;
    background: var(--mark-circle);
  }
  .back-mark .mark-name {
    font-weight: 800; font-size: 30px; color: var(--mark-blue); letter-spacing: .5px;
  }
  .back-web {
    position: absolute; left: 0; right: 0; bottom: 40px;
    text-align: center; font-size: 17px; color: var(--white); letter-spacing: .6px;
  }
  .back-web .web-name { color: var(--text-blue); }

  /* Front of card */
  .card-front { left: 520px; top: 450px; }
  .side-band {
    position: absolute; left: 0; top: 0; bottom: 0; width: 118px;
    background: var(--band-blue);
  }
  .side-line {
    position: absolute; left: 118px; top: 0; bottom: 0; width: 4px;
    background: var(--accent-line);
  }
  .ghost-circle {
    position: absolute; left: 395px; top: 45px;
    width: 230px; height: 210px; border-radius: 50%;
    background: var(--ghost-circle);
  }
  .front-circle {
    position: absolute; left: 80px; top: 62px;
    width: 80px; height: 80px; border-radius: 50%;
    background: var(--mark-circle);
    border: 3px solid var(--card-black);
  }
  .wordmark {
    position: absolute; left: 172px; top: 62px;
    font-weight: 800; font-size: 52px; line-height: 1;
    color: var(--mark-blue); letter-spacing: -.5px;
  }
  .contact-block {
    position: absolute; left: 200px; top: 150px;
    color: var(--soft-white);
  }
  .person-name {
    font-weight: 600; font-size: 22px; color: var(--text-blue); letter-spacing: 1px;
  }
  .person-title { font-size: 14px; margin-top: 2px; }
  .address { font-size: 14px; line-height: 1.4; margin-top: 10px; }
  .contact-list { list-style: none; margin-top: 10px; font-size: 14px; line-height: 1.5; }
  .contact-list li { display: flex; align-items: center; gap: 8px; }
  .contact-list svg { width: 11px; height: 11px; flex: none; }
  .contact-list .web-name { color: var(--text-blue); }
</style>
</head>
<body>
<main class="canvas">
  <section class="card card-back" aria-label="Card back">
    <div class="back-mark">
      <div class="mark-circle"></div>
      <div class="mark-name">Krovelmint</div>
    </div>
    <p class="back-web">www.<span class="web-name">krovelmint</span>.com</p>
  </section>

  <section class="card card-front" aria-label="Card front">
    <div class="ghost-circle"></div>
    <div class="side-band"></div>
    <div class="side-line"></div>
    <div class="front-circle"></div>
    <h1 class="wordmark">Krovelmint</h1>
    <div class="contact-block">
      <p class="person-name">Marek Olsen</p>
      <p class="person-title">Director</p>
      <p class="address">P.O. Box 4418<br>Fenwick Falls, MI 49377</p>
      <ul class="contact-list">
        <li>
          <svg viewBox="0 0 12 12"><path d="M2.5 1h2l1 3-1.3 1a6 6 0 0 0 2.8 2.8l1-1.3 3 1v2c0 .8-.7 1.5-1.5 1.5A9.5 9.5 0 0 1 1 2.5C1 1.7 1.7 1 2.5 1z" fill="var(--text-blue)"/></svg>
          +330 5812-3094
        </li>
        <li>
          <svg viewBox="0 0 12 12"><rect x="1" y="2.5" width="10" height="7" rx="1" fill="none" stroke="var(--text-blue)" stroke-width="1.3"/><path d="M1.5 3l4.5 3.5L10.5 3" fill="none" stroke="var(--text-blue)" stroke-width="1.3"/></svg>
          info@krovelmint.com
        </li>
        <li>
          <svg viewBox="0 0 12 12"><circle cx="6" cy="6" r="5" fill="none" stroke="var(--text-blue)" stroke-width="1.2"/><ellipse cx="6" cy="6" rx="2.2" ry="5" fill="none" stroke="var(--text-blue)" stroke-width="1"/><path d="M1 6h10" stroke="var(--text-blue)" stroke-width="1"/></svg>
          <span>www.<span class="web-name">krovelmint</span>.com</span>
        </li>
      </ul>
    </div>
  </section>
</main>
</body>
</html>
```